Design the Mobile Version of Existing Web Based Health Platform

Loomcrest is a social business enterprise that focus on public health by applying innovative healthcare services and consumer internet technology. Loomcrest offers a personalized platform of health promotion and disease prevention that puts the individual back in control of his life.

Loomcrest is looking for a Mobile Web UX/Visual Design professional to create a mobile version of Loomcrest website platform for iPhone, iPad/tablet and Android.

Contestants must to check www.loomcrest-demo.com.br to have a better understanding of Loomcrest Platform by creating an account (it's in portuguese, but anyone can get the general idea).

The mobile version of Loomcrest should have very similar functionality and user flows. This job is not to reengineer or re-imagine Loomcrest. It is just to reformat the existing functionality so it works well on mobile devices.

This description below is to help you to understand the core features of the platform (check the attachments to see the new web design of each one):

- Personally Controlled Health Record - PCHR enables an individual to own and manage a complete, secure, digital copy of her health and wellness information.
- Health Risk Assessments - is a process to estimate the nature and probability of adverse health effects, based on personal and family historical data, behavior and environment.
- Simulation of future health - "what if analysis" that emphasizes health education and behavior change.
- Step Quests - a program that gives you the opportunity to the participant to advance his personal well-being by doing simple Step Quests
- Health Alerts and Recommendations and Missing Data - Recommendations based on Wellbeing Bureau Guidelines and Federal Wellness Review Panel (FWRP), plus notifications to update outdated information.

The deliverable for this project is a psd file with a designed mobile version of Loomcrest.

A new design of the web platform is under construction. You can also check it looking at the files attached.

Target Market(s)

people 25-40 years old, 60% female, socially engaged

Industry/Entity Type

Healthcare

Requirements
Must have
• iPhone, iPad and Android version

Design must cover all current functionalities available on the web version (please, ensure you understand all features by creating an account at www.loomcrest-demo.com.br)

- Login/Sign up
- Welcome (first assessment)
- Add to Personal Controlled Health Record (PCHR)
- Update/Remove PCHR
- List PCHR
- Riskgrid (risk assessmen results)
- Simulation
- Alerts
- Missing data
- Recommendations
- StepQuest
- Badges
- Configurations

It's important to check the attachments to see how the web platform design is evolving.

```html
<!DOCTYPE html>
<html lang="pt">
<head>
<meta charset="utf-8">
<title>Loomcrest Mobile</title>
<link href="https://fonts.googleapis.com/css2?family=Open+Sans:ital,wght@0,400;0,600;0,700;1,600&display=swap" rel="stylesheet">
<style>
:root{
  --stage:#e6e6e6;
  --screen:#ffffff;
  --drawer:#e8eef6;
  --line:#c9d2de;
  --field:#c8d3e0;
  --ink:#8f98a3;
  --ink-dark:#5d6670;
  --grey-bar:#c7cad0;
  --orange:#f7943a;
  --orange-soft:#f8a65a;
  --footer:#e9eef5;
  --icon:#b7bfca;
  --photo:#7d8a93;
}
*{margin:0;padding:0;box-sizing:border-box}
html,body{width:1200px;height:768px;overflow:hidden}
body{background:radial-gradient(ellipse at 50% 40%,#fafafa 0%,var(--stage) 80%);font-family:"Open Sans",Arial,sans-serif;position:relative;color:var(--ink)}
.screen{position:absolute;background:var(--screen);overflow:hidden}
.screen--menu{left:296px;top:176px;width:248px;height:372px}
.screen--signup{left:648px;top:176px;width:247px;height:368px}
.abs{position:absolute}
.field{position:absolute;height:11px;border:1px solid var(--field);background:#fff;border-radius:1px}
.hdr{position:absolute;left:0;top:0;right:0;height:36px;background:#f4f6f9;border-bottom:1px solid var(--line)}
.ico{position:absolute;background:var(--icon);border-radius:3px}
.photo{position:absolute;background:linear-gradient(135deg,#9aa5ad,var(--photo));border-radius:2px}
/* drawer */
.drawer{position:absolute;left:0;top:0;width:176px;height:372px;background:var(--drawer);border-right:1px solid var(--line)}
.search{position:absolute;left:12px;top:12px;width:162px;height:19px;background:#fff;border:1px solid var(--line);font-size:6px;line-height:17px;padding-left:6px;color:#a3acb6}
.search svg{position:absolute;right:4px;top:3px}
.greet{position:absolute;left:12px;top:50px;width:160px;height:26px;border-top:1px solid var(--line);border-bottom:1px solid var(--line)}
.greet__text{position:absolute;left:33px;top:7px;font-size:7.5px;font-style:italic;font-weight:600;color:var(--ink)}
.menu{position:absolute;left:12px;top:76px;width:162px;list-style:none}
.menu__item{position:relative;height:32px;border-bottom:1px solid var(--line);font-size:8.5px;font-weight:700;line-height:32px;padding-left:32px;color:#98a1ac}
.menu__item .ico{left:0;top:6px;width:20px;height:20px}
/* signup */
.brand{position:absolute;left:12px;top:12px;display:flex;align-items:center;gap:4px;font-size:7px;font-weight:700;color:var(--orange)}
.brand__mark{width:10px;height:10px;background:var(--orange)}
.toplinks{position:absolute;left:62px;top:15px;font-size:5.5px;color:var(--orange)}
.toplinks span{color:var(--line);margin:0 4px}
.question{position:absolute;left:34px;top:64px;font-size:6.5px;font-weight:700;color:var(--ink-dark)}
.radio{position:absolute;left:36px;width:7px;height:7px;border:1px solid #b3bac3;border-radius:50%;background:#fff}
.radio--on::after{content:"";position:absolute;left:1.5px;top:1.5px;width:2px;height:2px;border-radius:50%;background:var(--orange)}
.option{position:absolute;left:48px;width:185px;height:11px;font-size:5px;font-weight:600;line-height:11px;padding-left:8px;color:#fff;background:var(--grey-bar)}
.option--active{background:var(--orange-soft)}
.check{position:absolute;right:14px;top:120px;font-size:4.5px;color:#aab2bb}
.check::before{content:"";display:inline-block;width:5px;height:5px;border:1px solid #b3bac3;margin-right:3px;vertical-align:-1px}
.label{position:absolute;left:34px;font-size:4.5px;font-weight:600;color:#9aa2ad}
.footer{position:absolute;left:0;top:266px;width:247px;height:102px;background:var(--footer);border-top:1px solid var(--line);font-size:3.6px;line-height:5.2px;color:#a2aab4}
.footer h4{font-size:4px;font-weight:700;letter-spacing:.3px;color:#a9b1ba;margin-bottom:5px}
.fcol{position:absolute;top:14px}
.social{position:absolute;width:10px;height:10px;border-radius:1px}
.next{position:absolute;left:184px;top:310px;width:51px;height:12px;background:var(--orange);color:#fff;font-size:4px;font-weight:700;line-height:12px;padding-left:6px}
</style>
</head>
<body>

<section class="screen screen--menu" aria-label="Menu lateral aberto">
  <div class="hdr"></div>
  <div class="ico" style="left:191px;top:12px;width:12px;height:12px"></div>
  <div class="photo" role="img" aria-label="Foto de perfil do usuário" style="left:210px;top:10px;width:16px;height:16px"></div>
  <svg class="abs" style="left:230px;top:16px" width="6" height="4"><path d="M0 0l3 3 3-3" fill="none" stroke="#9aa3ae"/></svg>
  <div class="field" style="left:184px;top:48px;width:51px"></div>
  <div class="abs" style="left:176px;top:80px;width:59px;height:10px;background:var(--grey-bar)"></div>
  <div class="abs" style="left:176px;top:93px;width:59px;height:10px;background:var(--grey-bar)"></div>
  <div class="abs" style="left:176px;top:106px;width:59px;height:10px;background:var(--orange-soft)"></div>
  <div class="abs" style="left:184px;top:122px;font-size:4px;color:#aab2bb">Não moro no Brasil</div>
  <div class="field" style="left:184px;top:136px;width:51px"></div>
  <div class="field" style="left:184px;top:150px;width:51px"></div>
  <div class="field" style="left:184px;top:164px;width:51px"></div>
  <div class="field" style="left:184px;top:178px;width:51px"></div>
  <div class="field" style="left:184px;top:192px;width:51px"></div>
  <div class="field" style="left:184px;top:206px;width:51px"></div>
  <div class="field" style="left:184px;top:220px;width:51px"></div>
  <div class="field" style="left:184px;top:234px;width:51px"></div>
  <div class="field" style="left:184px;top:248px;width:51px"></div>
  <div class="field" style="left:184px;top:262px;width:51px"></div>
  <div class="field" style="left:184px;top:280px;width:51px;font-size:4px;line-height:9px;padding-left:4px;color:#aab2bb">Female</div>
  <div class="field" style="left:184px;top:294px;width:51px"></div>
  <div class="next">NEXT</div>
  <div class="abs" style="left:176px;top:340px;width:72px;height:32px;background:var(--footer);font-size:4px;font-weight:700;color:#a9b1ba;padding:14px 0 0 13px">CONNECT WITH US</div>

  <nav class="drawer">
    <div class="search">Buscar
      <svg width="12" height="12"><circle cx="5" cy="5" r="3.5" fill="none" stroke="#aab2bb" stroke-width="1.2"/><path d="M7.6 7.6l3 3" stroke="#aab2bb" stroke-width="1.4"/></svg>
    </div>
    <div class="greet">
      <div class="photo" role="img" aria-label="Foto de perfil do usuário" style="left:0;top:3px;width:20px;height:20px"></div>
      <div class="greet__text">Good day, Tavimor !</div>
    </div>
    <ul class="menu">
      <li class="menu__item"><span class="ico"></span>Riskgrid</li>
      <li class="menu__item"><span class="ico"></span>Simulation</li>
      <li class="menu__item"><span class="ico" style="border-radius:50%"></span>Challenges</li>
      <li class="menu__item"><span class="ico"></span>Booklet</li>
      <li class="menu__item"><span class="ico"></span>Trophies</li>
      <li class="menu__item"><svg class="abs" style="left:1px;top:7px" width="18" height="18" fill="var(--icon)"><rect x="0" y="0" width="4" height="4"/><rect x="7" y="0" width="4" height="4"/><rect x="14" y="0" width="4" height="4"/><rect x="0" y="7" width="4" height="4"/><rect x="7" y="7" width="4" height="4"/><rect x="14" y="7" width="4" height="4"/><rect x="0" y="14" width="4" height="4"/><rect x="7" y="14" width="4" height="4"/><rect x="14" y="14" width="4" height="4"/></svg>More</li>
    </ul>
  </nav>
</section>

<section class="screen screen--signup" aria-label="Cadastro inicial">
  <header class="hdr">
    <div class="brand"><span class="brand__mark"></span>Loomcrest</div>
    <div class="toplinks">Consultations<span>|</span>Help</div>
    <div class="abs" style="left:134px;top:4px;width:1px;height:28px;background:var(--line)"></div>
    <svg class="abs" style="left:150px;top:12px" width="12" height="12" fill="var(--icon)"><rect width="3" height="3"/><rect x="4.5" width="3" height="3"/><rect x="9" width="3" height="3"/><rect y="4.5" width="3" height="3"/><rect x="4.5" y="4.5" width="3" height="3"/><rect x="9" y="4.5" width="3" height="3"/><rect y="9" width="3" height="3"/><rect x="4.5" y="9" width="3" height="3"/><rect x="9" y="9" width="3" height="3"/></svg>
    <svg class="abs" style="left:168px;top:11px" width="16" height="15"><path d="M6 0l6 11H0z" fill="var(--icon)"/><circle cx="12" cy="11" r="3.5" fill="var(--orange)"/></svg>
    <div class="ico" style="left:189px;top:12px;width:12px;height:12px"></div>
    <div class="photo" role="img" aria-label="Foto de perfil do usuário" style="left:209px;top:10px;width:16px;height:16px"></div>
    <svg class="abs" style="left:229px;top:16px" width="6" height="4"><path d="M0 0l3 3 3-3" fill="none" stroke="#9aa3ae"/></svg>
  </header>

  <div class="ico" style="left:19px;top:45px;width:8px;height:11px;border-radius:1px"></div>
  <div class="field" style="left:34px;top:45px;width:199px;font-size:4.5px;line-height:9px;padding-left:5px;color:#a3acb6">Add a new record</div>

  <div class="question">Como quer utilizar o Loomcrest?</div>
  <span class="radio" style="top:78px"></span><div class="option" style="top:76px">Vou usar meu LoomPass!</div>
  <span class="radio" style="top:92px"></span><div class="option" style="top:90px">Quero cuidar da minha saúde e posso trabalhar com o programa</div>
  <span class="radio radio--on" style="top:106px"></span><div class="option option--active" style="top:104px">Quero cuidar da minha saúde, mas eu não posso pagar nada</div>
  <div class="check">Não moro no Brasil</div>

  <div class="label" style="top:136px">Nome</div><div class="field" style="left:84px;top:134px;width:149px"></div>
  <div class="label" style="top:150px">Sobrenome</div><div class="field" style="left:84px;top:148px;width:149px"></div>
  <div class="label" style="top:164px">Data de nascimento</div><div class="field" style="left:84px;top:162px;width:149px"></div>
  <div class="label" style="top:178px">CEP</div><div class="field" style="left:84px;top:176px;width:149px"></div>
  <div class="label" style="top:192px">Estado</div><div class="field" style="left:84px;top:190px;width:149px"></div>
  <div class="label" style="top:206px">Cidade</div><div class="field" style="left:84px;top:204px;width:149px"></div>
  <div class="label" style="top:220px">Endereço</div><div class="field" style="left:84px;top:218px;width:149px"></div>
  <div class="label" style="top:234px">Bairro</div><div class="field" style="left:84px;top:232px;width:149px"></div>
  <div class="label" style="top:248px">Endereço</div><div class="field" style="left:84px;top:246px;width:149px"></div>
  <div class="label" style="top:262px">Bairro</div><div class="field" style="left:84px;top:260px;width:149px"></div>

  <footer class="footer">
    <div class="fcol" style="left:13px;width:42px"><h4>ABOUT US</h4>Lorem ipsum dolor sit amet, consectetur adipiscing elit. Morbi euismod placerat est in tincidunt. Sed sollicitudin mauris auctor. Phasellus ut ultricies nisl.</div>
    <div class="fcol" style="left:61px"><h4>EXPLORE</h4>Home<br>About Us<br>Services<br>Partner<br>Blog</div>
    <div class="fcol" style="left:108px"><h4>BROWSE</h4>Careers<br>Press &amp; Media<br>Contact Us<br>Terms of Service<br>Privacy Policy</div>
    <div class="fcol" style="left:149px"><h4>CONTACT US</h4>Loomcrest<br>Rua Lumen 240<br>Curitiba - PR<br><br>Phone<br>041 5550 0123<br><br>Fax<br>041 5550 0456</div>
    <div class="fcol" style="left:188px"><h4>CONNECT WITH US</h4></div>
    <span class="social" style="left:190px;top:24px;background:#d9534f"></span>
    <span class="social" style="left:206px;top:24px;background:#6fb3d9"></span>
    <span class="social" style="left:222px;top:24px;background:#fff;border:1px solid var(--line)"></span>
    <span class="social" style="left:190px;top:39px;background:#d9534f"></span>
    <span class="social" style="left:206px;top:39px;background:#4a67a8"></span>
    <span class="social" style="left:222px;top:39px;background:#4aa8e0"></span>
  </footer>
</section>

</body>
</html>
```